Need a redesign for our Wordpress Credit report website

Hi, We need someone to redesign our Wordpress credit report website, brightledgerview.co.za. The designer will be responsible for the following pages:
- home page
- blog page
- single post
- dashboard
- credit report page

About BrightLedgerView.co.za
Bright Ledger View is a consumer focussed credit report platform where South African citizens can get an easy to understand credit report that shows them where to improve their credit scores.

```html
<!DOCTYPE html>
<html lang="en">
<head>
<meta charset="utf-8">
<title>Bright Ledger View — Check Your Credit Score</title>
<link href="https://fonts.googleapis.com/css2?family=Nunito:wght@400;600;700;800&display=swap" rel="stylesheet">
<style>
:root{
  --ink:#1f2b2b;
  --muted:#8a9296;
  --green:#6cb97a;
  --green-text:#58ad6c;
  --green-soft:#e4f3e7;
  --hero-bg:#f5f7fa;
  --line:#d9dee3;
  --card:#ffffff;
  --footer:#1f2c26;
  --footer-text:#c9d1cc;
  --star:#f5b400;
  --pink:#e8336f;
  --purple:#8a5cd6;
  --blue:#4f8fe8;
  --mint:#4fd69a;
}
*{box-sizing:border-box;margin:0;padding:0}
html,body{width:1200px;height:3119px;overflow:hidden}
body{font-family:"Nunito",sans-serif;color:var(--ink);background:#fff;position:relative}
.section{position:relative;width:1200px}
.abs{position:absolute}

/* header + hero */
.hero{height:740px;background:var(--hero-bg)}
.brand{left:112px;top:44px;display:flex;align-items:center;gap:8px;font-size:18px;font-weight:700;color:var(--ink)}
.brand-dot{width:14px;height:14px;border-radius:50%;background:var(--green)}
.nav{left:620px;top:46px;display:flex;align-items:center;gap:0}
.nav a{font-size:13px;color:var(--ink);text-decoration:none;font-weight:600;width:94px;text-align:center}
.nav a.active{color:var(--green-text)}
.login{left:983px;top:40px;width:105px;height:36px;border-radius:8px;background:var(--green);color:#fff;font-size:13px;font-weight:700;display:flex;align-items:center;justify-content:center;box-shadow:0 4px 10px rgba(108,185,122,.35)}
.eyebrow{font-size:13px;font-weight:700;color:var(--green-text)}
.hero-title{left:112px;top:180px;font-size:35px;line-height:46px;font-weight:800}
.field{height:35px;border:1px solid var(--line);border-radius:4px;background:#fff;font-size:10px;color:#a3aab0;padding:0 14px;display:flex;align-items:center}
.field.focus{border:2px solid var(--green)}
.agree{left:115px;top:446px;display:flex;align-items:center;gap:10px;font-size:10.5px;color:#555}
.agree span.box{width:13px;height:13px;border:1px solid #b8bec4;border-radius:2px}
.cta{left:115px;top:479px;width:375px;height:35px;background:var(--green);border-radius:4px;color:#fff;font-size:11px;font-weight:700;display:flex;align-items:center;justify-content:center}
.fine{left:115px;top:532px;width:375px;font-size:8px;line-height:10px;color:#7a8286;text-align:center}
.perk{display:flex;align-items:center;gap:12px;font-size:10.5px;line-height:13px;color:#444}
.perk svg{flex:none}

.score-card{left:599px;top:143px;width:489px;height:285px;background:#fff;border-radius:10px;box-shadow:0 8px 30px rgba(30,50,80,.07)}
.score-label{font-size:11px;font-weight:700}
.score-name{font-size:10px;font-weight:700;color:var(--green-text)}
.legend{display:flex;gap:0}
.legend div{width:44px;text-align:center;font-size:7.5px;color:#a7adb2}
.legend i{display:block;width:20px;height:7px;border-radius:4px;margin:0 auto 6px}
.phone{left:873px;top:175px;width:182px;height:387px;background:#fff;border:4px solid #8c97a4;border-radius:18px;box-shadow:0 10px 30px rgba(30,50,80,.12);overflow:hidden}
.phone-table{position:absolute;left:14px;right:14px;top:212px;font-size:5.6px;color:#555}
.phone-table div{display:flex;justify-content:space-between;height:14.5px;border-bottom:1px solid #eef0f2;align-items:center}
.trend{left:634px;top:440px;width:224px;height:97px;background:#fff;border-radius:10px;box-shadow:0 8px 24px rgba(30,50,80,.07)}

/* features */
.features{height:590px;background:#fff}
.center{left:0;width:1200px;text-align:center}
.h2{font-size:27px;font-weight:800}
.feat{width:200px;text-align:center}
.feat-icon{width:70px;height:70px;margin:0 auto;border-radius:14px;background:linear-gradient(135deg,var(--green-soft),#f4faf5)}
.feat h3{margin-top:30px;font-size:12px;font-weight:700}
.feat p{margin-top:8px;font-size:10.5px;color:var(--muted)}

/* testimonials */
.testimonials{height:740px;background:var(--hero-bg)}
.tabs{display:flex;justify-content:center;gap:14px;font-size:11px;font-weight:700;color:var(--green-text)}
.tabs span.sep{color:#c4cad0;font-weight:400}
.quote{background:#fff;border-radius:6px;box-shadow:0 6px 20px rgba(30,50,80,.06);padding:18px 16px}
.quote-top{display:flex;justify-content:space-between;align-items:center}
.qmark{font-size:34px;font-weight:800;color:#dfe9e2;line-height:20px;height:20px}
.stars{color:var(--star);font-size:14px;letter-spacing:1px}
.quote p{margin-top:16px;font-size:10.4px;line-height:15px;color:#7d858a;text-align:justify}
.author{position:absolute;left:16px;bottom:14px;right:16px;display:flex;align-items:center;justify-content:space-between;font-size:11.5px;font-weight:700}
.avatar{width:38px;height:38px;border-radius:50%;background:linear-gradient(135deg,#c9a58c,#5b4a42)}
.review{background:#fff;border-radius:6px;box-shadow:0 6px 20px rgba(30,50,80,.06);padding:20px 14px 0 62px;height:103px}
.review .avatar{position:absolute;left:12px;top:22px}
.review-head{display:flex;justify-content:space-between;font-size:11px;font-weight:700}
.review-head em{font-style:normal;font-weight:600;color:var(--green-text);font-size:10px}
.review p{margin-top:6px;font-size:10px;line-height:12.5px;color:#7d858a}
.dot{width:6px;height:6px;border-radius:50%;background:#cfe6d4}
.dot.on{background:var(--green)}
.pay{width:140px;text-align:center;font-size:13px;font-weight:700;color:#8d9398;display:flex;align-items:center;justify-content:center;gap:8px}
.pay i{width:22px;height:22px;border-radius:50%;background:#a9aeb3}

/* reasons */
.reasons{height:640px;background:#fff}
.reason{width:215px}
.reason-icon{width:80px;height:74px;border-radius:14px;background:linear-gradient(135deg,var(--green-soft),#f5faf6)}
.reason h3{margin-top:38px;font-size:12px;line-height:15px;font-weight:800}
.reason p{margin-top:20px;font-size:10.4px;line-height:18px;color:#80888d;text-align:justify}
.more{left:829px;top:492px;font-size:12px;font-weight:700;color:var(--green-text)}

/* footer */
.footer{height:409px;background:var(--footer);color:var(--footer-text)}
.footer .brand{left:170px;top:60px;color:#fff}
.f-about{left:170px;top:118px;width:190px;font-size:10px;line-height:15px}
.f-phone{left:170px;top:186px;display:flex;gap:12px;align-items:center;font-size:12px;font-weight:800;letter-spacing:2px;color:#fff}
.f-addr{left:170px;top:218px;font-size:10px;line-height:15px;width:190px}
.f-loc{left:170px;top:264px;display:flex;gap:12px;align-items:center;font-size:10.5px;font-weight:800;color:#fff}
.f-col h4{font-size:11.5px;font-weight:700;color:#fff;margin-bottom:20px}
.f-col a{display:block;font-size:9.5px;color:var(--footer-text);text-decoration:none;margin-bottom:13px}
.social{display:grid;grid-template-columns:72px 72px;row-gap:22px}
.social span{font-size:9px;font-weight:700;color:#fff;display:flex;align-items:center;gap:5px}
.social i{width:8px;height:8px;border-radius:50%;background:#fff}
.f-bottom{left:170px;top:345px;font-size:9px;display:flex;gap:14px;align-items:center}
.f-copy{right:170px;top:345px;font-size:9px;color:#fff}
.f-copy b{color:var(--green);font-weight:600}
</style>
</head>
<body>

<section class="section hero">
  <div class="abs brand"><span class="brand-dot"></span>Bright Ledger View</div>
  <nav class="abs nav">
    <a class="active" href="#">Home</a><a href="#">Articles</a><a href="#">About</a><a href="#">Contact</a>
  </nav>
  <div class="abs login">Login</div>

  <div class="abs eyebrow" style="left:112px;top:148px">Modern tools to help you calculate credit score</div>
  <h1 class="abs hero-title">Check Your Credit Score<br>Within Seconds</h1>

  <div class="abs field focus" style="left:115px;top:290px;width:375px">ID Number</div>
  <div class="abs field" style="left:115px;top:344px;width:179px">First Name</div>
  <div class="abs field" style="left:311px;top:344px;width:179px">Last Name</div>
  <div class="abs field" style="left:115px;top:395px;width:179px">Email</div>
  <div class="abs field" style="left:311px;top:395px;width:179px">Phone Number</div>
  <div class="abs agree"><span class="box"></span>I agree with the terms and conditions</div>
  <div class="abs cta">Show My Score</div>
  <p class="abs fine">By signing up and agreeing with the terms you authorise BrightLedgerView.co.za<br>to request your credit report from the bureaus and display it within the site.</p>

  <div class="abs score-card">
    <div class="abs" style="left:20px;top:20px"><div class="score-label">Credit Score</div><div class="score-name">Daniel</div></div>
    <svg class="abs" style="left:20px;top:30px" width="240" height="175" viewBox="0 0 240 175">
      <defs><linearGradient id="arcGrad" x1="0" x2="1"><stop offset="0" stop-color="#e8336f"/><stop offset=".45" stop-color="#8a5cd6"/><stop offset=".8" stop-color="#4f8fe8"/><stop offset="1" stop-color="#4fd69a"/></linearGradient></defs>
      <path d="M40,135 A85,85 0 1,1 200,85" fill="none" stroke="url(#arcGrad)" stroke-width="6" stroke-linecap="round"/>
      <circle cx="200" cy="85" r="6" fill="#fff" stroke="#4fd69a" stroke-width="3"/>
      <circle cx="120" cy="105" r="50" fill="#fff" stroke="#eef0f3" stroke-width="8"/>
      <text x="120" y="108" text-anchor="middle" font-family="Nunito,sans-serif" font-size="30" font-weight="800" fill="#1f2b2b">760</text>
      <text x="120" y="126" text-anchor="middle" font-family="Nunito,sans-serif" font-size="12" font-weight="700" font-style="normal" fill="#58ad6c">Excellent</text>
      <path d="M170,68 L184,72 L176,84 Z" fill="#1f2b2b"/>
      <text x="126" y="12" font-family="Nunito,sans-serif" font-size="7" fill="#8a5cd6">580</text>
      <text x="168" y="24" font-family="Nunito,sans-serif" font-size="7" fill="#4f8fe8">640</text>
      <text x="196" y="50" font-family="Nunito,sans-serif" font-size="7" fill="#4f8fe8">700</text>
      <text x="6" y="110" font-family="Nunito,sans-serif" font-size="7" fill="#e8336f">300</text>
      <text x="222" y="110" font-family="Nunito,sans-serif" font-size="7" fill="#999">850</text>
    </svg>
    <div class="abs legend" style="left:14px;top:240px">
      <div><i style="background:var(--pink)"></i>Poor</div>
      <div><i style="background:var(--purple)"></i>Fair</div>
      <div><i style="background:var(--blue)"></i>Good</div>
      <div><i style="background:var(--mint)"></i>Excellent</div>
      <div><i style="background:var(--green)"></i>Perfect</div>
    </div>
  </div>

  <div class="abs trend">
    <svg width="224" height="97" viewBox="0 0 224 97">
      <defs><linearGradient id="lineGrad" x1="0" x2="1"><stop offset="0" stop-color="#4fd69a"/><stop offset="1" stop-color="#4f8fe8"/></linearGradient></defs>
      <path d="M25,80 C55,40 70,45 90,50 C120,58 150,80 200,20" fill="none" stroke="url(#lineGrad)" stroke-width="3" stroke-linecap="round"/>
      <circle cx="90" cy="50" r="6" fill="#fff" stroke="#4f8fe8" stroke-width="3"/>
      <rect x="68" y="14" width="52" height="18" rx="9" fill="#fff" stroke="#4fd69a"/>
      <text x="94" y="27" text-anchor="middle" font-family="Nunito,sans-serif" font-size="10" fill="#1f2b2b">700</text>
    </svg>
  </div>

  <div class="abs phone">
    <div class="abs" style="left:14px;top:16px"><div class="score-label" style="font-size:10px">Credit Score</div><div class="score-name" style="font-size:9px">Daniel</div></div>
    <svg class="abs" style="left:20px;top:42px" width="140" height="110" viewBox="0 0 140 110">
      <path d="M22,88 A52,52 0 1,1 118,56" fill="none" stroke="url(#arcGrad)" stroke-width="4" stroke-linecap="round"/>
      <circle cx="118" cy="56" r="4" fill="#fff" stroke="#4fd69a" stroke-width="2"/>
      <circle cx="70" cy="70" r="30" fill="#fff" stroke="#eef0f3" stroke-width="5"/>
      <text x="70" y="72" text-anchor="middle" font-family="Nunito,sans-serif" font-size="18" font-weight="800" fill="#1f2b2b">760</text>
      <text x="70" y="84" text-anchor="middle" font-family="Nunito,sans-serif" font-size="7" font-weight="700" fill="#58ad6c">Excellent</text>
      <path d="M102,46 L110,48 L105,55 Z" fill="#1f2b2b"/>
    </svg>
    <div class="abs legend" style="left:6px;top:165px;transform:scale(.62);transform-origin:left top">
      <div><i style="background:var(--pink)"></i>Poor</div>
      <div><i style="background:var(--purple)"></i>Fair</div>
      <div><i style="background:var(--blue)"></i>Good</div>
      <div><i style="background:var(--mint)"></i>Excellent</div>
      <div><i style="background:var(--green)"></i>Perfect</div>
    </div>
    <div class="phone-table">
      <div><span>Addresses</span><span>6</span></div>
      <div><span>Phone Number</span><span>10</span></div>
      <div><span>Employers</span><span>5</span></div>
      <div><span>Previous Enquiries</span><span>17</span></div>
      <div><span>Loan Account</span><span>1</span></div>
      <div><span>Outstanding Loan Value</span><span>$ 0.00</span></div>
      <div><span>Loan Installment</span><span>$ 0.00</span></div>
      <div><span>Retail Account</span><span>1</span></div>
      <div><span>Retail Account Value</span><span>$ 0.00</span></div>
      <div><span>Retail Account Installment</span><span>$ 0.00</span></div>
      <div><span>Judgement</span><span>760</span></div>
    </div>
  </div>

  <div class="abs perk" style="left:174px;top:626px">
    <svg width="32" height="28" viewBox="0 0 32 28" fill="none" stroke="#4f8fe8" stroke-width="1.4"><rect x="2" y="3" width="22" height="18" rx="2"/><line x1="2" y1="8" x2="24" y2="8"/><circle cx="24" cy="20" r="6" fill="#fff"/><path d="M24,17 v3 h2"/></svg>
    <span>See your most recent<br>credit score</span></div>
  <div class="abs perk" style="left:430px;top:626px">
    <svg width="28" height="30" viewBox="0 0 28 30" fill="none" stroke="#4f8fe8" stroke-width="1.4"><circle cx="12" cy="8" r="5"/><path d="M3,27 c0-8 4-11 9-11 s9,3 9,11"/><circle cx="21" cy="22" r="5" fill="#fff"/><path d="M21,19.5 v5 M18.5,22 h5"/></svg>
    <span>Get access to your<br>full credit profile</span></div>
  <div class="abs perk" style="left:604px;top:626px">
    <svg width="32" height="30" viewBox="0 0 32 30" fill="none" stroke="#8a5cd6" stroke-width="1.4"><circle cx="10" cy="8" r="4"/><circle cx="22" cy="8" r="4"/><path d="M2,26 c0-7 3-10 8-10 s8,3 8,10 M14,26 c0-7 3-10 8-10 s8,3 8,10"/></svg>
    <span>See who has been<br>looking at your profile</span></div>
  <div class="abs perk" style="left:798px;top:626px">
    <svg width="30" height="30" viewBox="0 0 30 30" fill="none" stroke="#e8336f" stroke-width="1.4"><rect x="3" y="3" width="7" height="14" rx="1"/><path d="M10,5 h10 c3,0 5,2 5,5 l-2,7 h-6 l1,7 c0,2-2,3-3,2 l-5-8"/></svg>
    <span>See if you have any<br>adverse or Blacklistings</span></div>
</section>

<section class="section features">
  <div class="abs center eyebrow" style="top:50px;font-size:12px">Most wanted things you can't missed</div>
  <h2 class="abs center h2" style="top:74px">Our Key Features</h2>

  <div class="abs feat" style="left:191px;top:163px"><div class="feat-icon" role="img" aria-label="Line icon of two people resolving a dispute"></div><h3>Dispute Generator</h3><p>Easily manage disputes</p></div>
  <div class="abs feat" style="left:403px;top:163px"><div class="feat-icon" role="img" aria-label="Line icon of a calculator and bills"></div><h3>Budget Tool</h3><p>Easily create a budget</p></div>
  <div class="abs feat" style="left:606px;top:163px"><div class="feat-icon" role="img" aria-label="Line icon of a rising chart held in a hand"></div><h3>Improve</h3><p>Your credit score eBook</p></div>
  <div class="abs feat" style="left:808px;top:163px"><div class="feat-icon" role="img" aria-label="Line icon of a secured spreadsheet document"></div><h3>Personal Budgeting</h3><p>Budgeting Spreadsheet</p></div>
  <div class="abs feat" style="left:282px;top:358px"><div class="feat-icon" role="img" aria-label="Line icon of a score speedometer"></div><h3>Perfect Score</h3><p>Video course</p></div>
  <div class="abs feat" style="left:499px;top:358px"><div class="feat-icon" role="img" aria-label="Line icon of a person with finance charts"></div><h3>Personal Finance</h3><p>Video Tutorials</p></div>
  <div class="abs feat" style="left:716px;top:358px"><div class="feat-icon" role="img" aria-label="Line icon of a 24/7 support phone"></div><h3>24/7 Support</h3><p>Dedicated 24/7 Support</p></div>
</section>

<section class="section testimonials">
  <h2 class="abs center h2" style="top:58px">What They Say</h2>
  <div class="abs center tabs" style="top:113px;display:flex"><span>User Testimonials</span><span class="sep">|</span><span>Verified Reviews</span></div>

  <div class="abs quote" style="left:222px;top:164px;width:174px;height:298px">
    <div class="quote-top"><span class="qmark">“</span><span class="stars">★★★★★</span></div>
    <p>The report was accurate and gave me a good understanding of my current credit status. I found it interesting the way the scoring worked and really enjoyed reading it...guess because I am doing well with managing credit.</p>
    <div class="author"><div class="avatar" role="img" aria-label="Portrait photo of the reviewer"></div><span>Marisa Delport</span></div>
  </div>
  <div class="abs quote" style="left:411px;top:164px;width:174px;height:298px">
    <div class="quote-top"><span class="qmark">“</span><span class="stars">★★★★★</span></div>
    <p>The report is well detailed, and gives you all the info that you need. This has helped me to restructure some finances and improve. I would like to highly recommend using BrightLedgerView.co.za to anyone interested in knowing what their score is.</p>
    <div class="author"><div class="avatar" role="img" aria-label="Portrait photo of the reviewer" style="background:linear-gradient(135deg,#e6c3a0,#9b6a4a)"></div><span>Tobias Renke</span></div>
  </div>
  <div class="abs" style="left:373px;top:491px;display:flex;gap:14px"><span class="dot on"></span><span class="dot"></span><span class="dot"></span></div>

  <div class="abs review" style="left:614px;top:164px;width:362px">
    <div class="avatar" role="img" aria-label="Portrait photo of the reviewer"></div>
    <div class="review-head"><span>Lienke Swanepoel • <em>28 review</em></span><span class="stars">★★★★★</span></div>
    <p>The credit report is easy to use, informative and accurate to the date. Helps me to manage my financial well-being.</p>
  </div>
  <div class="abs review" style="left:614px;top:285px;width:362px">
    <div class="avatar" role="img" aria-label="Portrait photo of the reviewer" style="background:linear-gradient(135deg,#b9c4cc,#56636c)"></div>
    <div class="review-head"><span>Carla Oosthuizen • <em>16 review</em></span><span class="stars">★★★★★</span></div>
    <p>Their customer support team has been very impressive. The tools and knowledge they shared were of great practical use.</p>
  </div>
  <div class="abs review" style="left:614px;top:406px;width:362px">
    <div class="avatar" role="img" aria-label="Portrait photo of the reviewer" style="background:linear-gradient(135deg,#a07a62,#3d2f29)"></div>
    <div class="review-head"><span>Thabo Mokoena • <em>10 review</em></span><span class="stars">★★★★★</span></div>
    <p>A very user friendly service and provides a timely credit report allaying your fears of knowing your credit worthiness</p>
  </div>
  <div class="abs" style="left:993px;top:308px;display:flex;flex-direction:column;gap:14px"><span class="dot on"></span><span class="dot"></span><span class="dot"></span></div>

  <div class="abs center eyebrow" style="top:563px;font-size:11px">Trusted by the best companies in the worlds</div>
  <div class="abs pay" style="left:316px;top:620px"><i></i>Orbitpay</div>
  <div class="abs pay" style="left:450px;top:620px"><i></i>Tandempay</div>
  <div class="abs pay" style="left:596px;top:620px"><i></i>Walletline</div>
  <div class="abs pay" style="left:734px;top:620px"><i></i>Veriscard</div>
</section>

<section class="section reasons">
  <div class="abs center eyebrow" style="top:68px;font-size:12px">Why get your score from us?</div>
  <h2 class="abs center h2" style="top:92px">Reason and Facts</h2>

  <div class="abs reason" style="left:260px;top:181px">
    <div class="reason-icon" role="img" aria-label="Line icon of a locked card"></div>
    <h3>We don't abuse your<br>personal information</h3>
    <p>Companies that give out free credit scores use your personal information to sell you financial products. That's how they can afford to give it to you for free. We believe that your personal information should be protected and not abused. That's why we ask a small fee. It enables us to protect your information and not abuse it.</p>
  </div>
  <div class="abs reason" style="left:513px;top:181px">
    <div class="reason-icon" role="img" aria-label="Line icon of a report with charts"></div>
    <h3>Our report is super easy<br>to understand</h3>
    <p>Our credit report is one of the easiest reports to understand. The report is clearly laid out and you will see immediately if you can apply for finance, if you are blacklisted, and where you can improve.</p>
  </div>
  <div class="abs reason" style="left:767px;top:181px">
    <div class="reason-icon" role="img" aria-label="Line icon of a handshake"></div>
    <h3>300,000 + South Africans<br>have trusted us</h3>
    <p>Since 2008 we have helped over 300,000 South Africans make sense of their credit reports, so you can rest assured knowing that we have a proven track record and that you are in safe hands with us.</p>
  </div>
  <div class="abs more" style="left:791px">View more about us &nbsp;&nbsp;›</div>
</section>

<footer class="section footer">
  <div class="abs brand"><span class="brand-dot"></span>Bright Ledger View</div>
  <p class="abs f-about">If you have any questions or need help, feel free to contact with our team.</p>
  <div class="abs f-phone"><svg width="12" height="12" viewBox="0 0 24 24" fill="#fff"><path d="M6.6 10.8a15 15 0 0 0 6.6 6.6l2.2-2.2c.3-.3.7-.4 1-.2 1.1.4 2.3.6 3.6.6.6 0 1 .4 1 1V20c0 .6-.4 1-1 1A17 17 0 0 1 3 4c0-.6.4-1 1-1h3.5c.6 0 1 .4 1 1 0 1.3.2 2.5.6 3.6.1.3 0 .7-.2 1z"/></svg>+27 21 555 0142</div>
  <p class="abs f-addr">18 Kloofnek Lane; Gardens,<br>Cape Town 8001.</p>
  <div class="abs f-loc"><svg width="11" height="13" viewBox="0 0 24 28" fill="#fff"><path d="M12 0a10 10 0 0 0-10 10c0 7.5 10 18 10 18s10-10.5 10-18A10 10 0 0 0 12 0zm0 14a4 4 0 1 1 0-8 4 4 0 0 1 0 8z"/></svg>Get Our Location</div>

  <div class="abs f-col" style="left:457px;top:74px"><h4>Terms</h4><a>General Terms Of Use</a><a>Exclusion Of Liability</a><a>Security Policy</a><a>Privacy Policy</a></div>
  <div class="abs f-col" style="left:589px;top:74px"><h4>Purchase</h4><a>Delivery Policy</a><a>Data Policy</a><a>Refund Policy</a><a>Charges And Fees</a></div>
  <div class="abs f-col" style="left:719px;top:74px"><h4>Quick Links</h4><a>About Us</a><a>Articles</a><a>Contact Us</a><a>Login</a></div>
  <div class="abs f-col" style="left:861px;top:74px"><h4>Follow Us</h4>
    <div class="social"><span><i></i>Friendline</span><span><i></i>ClipStream</span><span><i></i>SlideCast</span><span><i></i>AirWave</span></div>
  </div>

  <div class="abs f-bottom"><span>Terms &amp; Conditions</span><span>•</span><span>Privacy Policy</span><span>•</span><span>Sitemap</span></div>
  <div class="abs f-copy">©2022 BrightLedgerView, All Rights Reserved. With Love by <b>Northgate Studio</b></div>
</footer>

</body>
</html>
```